Company Letter head for real estate company

need company letter head
Updates

You can use the logo that I submitted. no need to create a new one

Requirements
Must have
• must have my address on it..38264 WINDMERE, ELMWOOD, ND 48302-1175, INFO@MUVRO.CA

```html
<!DOCTYPE html>
<html lang="en">
<head>
<meta charset="utf-8">
<title>Muvro Letterhead</title>
<link href="https://fonts.googleapis.com/css2?family=Open+Sans:wght@400;600&family=Lato:wght@400&display=swap" rel="stylesheet">
<style>
  :root {
    --backdrop: #dcdfe6;
    --paper: #ffffff;
    --brand-green: #8cc63e;
    --icon-green: #4f8b1c;
    --ink: #555555;
    --ink-dark: #222222;
    --rule: #444444;
    --signature-tone: #e6e6e6;
  }
  * { margin: 0; padding: 0; box-sizing: border-box; }
  html, body {
    width: 1062px; height: 1200px; overflow: hidden;
    background: var(--backdrop);
  }
  .letterhead {
    position: absolute; left: 234px; top: 260px;
    width: 595px; height: 767px;
    background: var(--paper);
    font-family: "Open Sans", sans-serif;
    color: var(--ink);
  }
  .band { position: absolute; left: 0; width: 100%; height: 11px; background: var(--brand-green); }
  .band--top { top: 0; }
  .band--bottom { bottom: 0; }

  .brand {
    position: absolute; top: 34px; left: 0; width: 100%;
    display: flex; justify-content: center; align-items: center; gap: 10px;
  }
  .brand__dot { width: 22px; height: 22px; border-radius: 50%; background: var(--brand-green); }
  .brand__name {
    font-family: "Open Sans", sans-serif; font-weight: 600;
    font-size: 26px; letter-spacing: 2px; color: var(--ink-dark);
  }

  .block { position: absolute; left: 56px; width: 481px; font-size: 9.6px; }
  .date { top: 150px; }
  .recipient { top: 174px; line-height: 11.7px; }
  .salutation { top: 240px; }
  .body-copy { line-height: 17.2px; text-align: justify; hyphens: auto; }
  .p1 { top: 274px; }
  .p2 { top: 377px; }
  .p3 { top: 446px; }
  .closing { top: 533px; }
  .signature {
    position: absolute; left: 56px; top: 558px; width: 136px; height: 16px;
    background: var(--signature-tone); border-radius: 3px;
  }
  .signer { top: 581px; font-size: 12px; font-weight: 600; }
  .signer-role { top: 601px; }

  .contact-rule {
    position: absolute; left: 56px; top: 727px; width: 468px; height: 1px; background: var(--rule);
  }
  .contact {
    position: absolute; top: 733px; left: 61px; width: 462px;
    display: flex; align-items: center; justify-content: space-between;
    font-family: "Lato", sans-serif; font-size: 11.5px; color: var(--ink-dark);
  }
  .contact__item { display: flex; align-items: center; gap: 3px; white-space: nowrap; }
  .contact__item--address { font-size: 12px; }
  .contact__item svg { fill: var(--icon-green); flex: none; }
</style>
</head>
<body>
  <main class="letterhead">
    <div class="band band--top"></div>

    <header class="brand">
      <span class="brand__dot"></span>
      <span class="brand__name">MUVRO</span>
    </header>

    <p class="block date">Issuing Date: May 5, 2018</p>
    <p class="block recipient">Name Of Employee Mr. XYZABC<br>Address of Employee<br>Address Line 2 etc..</p>
    <p class="block salutation">Dear Mr.XYZABC</p>

    <p class="block body-copy p1">Lorem Ipsum has been the industry's standard dummy text ever since the 1500s, when an unknown printer took a galley of type and scrambled it to make a type specimen book. It has survived not only five centuries, but also the leap into electronic typesetting, remaining essentially unchanged. It was popularised in the 1960s with the release of transfer sheets containing Lorem Ipsum passages, and more recently with desktop publishing software like modern page layout tools including versions of Lorem Ipsum.</p>
    <p class="block body-copy p2">Lorem Ipsum is simply dummy text of the printing and typesetting industry. Lorem Ipsum has been the industry's standard dummy text ever since the 1500s, when an unknown printer took a galley of type and scrambled it to make a type specimen book.</p>
    <p class="block body-copy p3">It has survived not only five centuries, but also the leap into electronic typesetting, remaining essentially unchanged. It was popularised in the 1960s with the release of transfer sheets containing Lorem IpsumIpsum passages.</p>

    <p class="block closing">Yours Sincerely</p>
    <div class="signature" role="img" aria-label="Handwritten signature of Dorian Vale"></div>
    <p class="block signer">Dorian Vale</p>
    <p class="block signer-role">Managing Director</p>

    <div class="contact-rule"></div>
    <footer class="contact">
      <span class="contact__item">
        <svg width="11" height="9" viewBox="0 0 11 9"><path d="M0 2.5C2 0 9 0 11 2.5L9.5 4 8 3V2H3v1L1.5 4z"/><path d="M2.5 4h6l1 5h-8z"/></svg>
        48302-1175
      </span>
      <span class="contact__item">
        <svg width="11" height="8" viewBox="0 0 11 8"><rect width="11" height="8"/><path d="M0 0l5.5 4.5L11 0" stroke="#fff" stroke-width="1" fill="none"/></svg>
        info@muvro.ca
      </span>
      <span class="contact__item">
        <svg width="11" height="11" viewBox="0 0 11 11"><circle cx="5.5" cy="5.5" r="5.5"/><path d="M2.5 3.5l2-1 1 1.5-1 1.5 1 2-1.5 1-1-2zM6.5 2l2 1-0.5 2 1 1.5-2 1z" fill="#fff"/></svg>
        www.muvro.ca
      </span>
      <span class="contact__item contact__item--address">
        <svg width="10" height="14" viewBox="0 0 10 14"><path d="M5 0a5 5 0 0 1 5 5c0 3.5-5 9-5 9S0 8.5 0 5a5 5 0 0 1 5-5z"/><circle cx="5" cy="5" r="1.8" fill="#fff"/></svg>
        38264 WINDMERE, ELMWOOD, ND
      </span>
    </footer>

    <div class="band band--bottom"></div>
  </main>
</body>
</html>
```